VEMRA - new private security company in Guyana, South America needs a website & logo design

New private security company in Guyana needs a website ready for the company launch. The business will offer armed and unarmed security to high net worth individuals, politicians, government officials, diplomats and off-shore oil industry vessels and platforms.

The company has its own heliport and indoor training range, armoured vehicles, ambulances and uniformed security personnel, and we would like some imager to indicate this.

The team leaders are all ex-special forces.

The website structure should be something like:

PAGE 1 Home
PAGE 2 About Us
PAGE 3 Guyana Security Overview
PAGE 4 Services
PAGE 5 Contact Us
PAGE 6 Useful Links

We have uploaded a file with the text copy for each of these pages.

The web domain has been registered through Pellnet and is www.vemra.group

Target Market(s)

Corporations involved in the oil and gas industry, Embassies, Investment companies and individuals, Caribbean diaspora.

Industry/Entity Type

Security Service

Logo Text

VEMRA

Coding

Coded - Design and coding required

Number of Pages Required

5+ page

Font styles to use
Sans Serif

Requirements
Must have
• Must have:
an enquiry/contact form page
general location map: https://mapfold.example/loc/Kp82wQzLr5Ynb7Xh4;
text as per web content document uploaded to this site
Nice to have
• Images of private security (cars, bodyguards, helicopters/planes, etc)
Images of Maritime security (non-military)
Images of people of colour (Guyana has mainly afro and indian residents)
Image of a high tec security control room

```html
<!DOCTYPE html>
<html lang="en">
<head>
<meta charset="utf-8">
<title>VEMRA Security – Services</title>
<link rel="stylesheet" href="https://fonts.googleapis.com/css2?family=Oswald:wght@400;500;600;700&family=Lato:wght@400;700&display=swap">
<style>
  :root{
    --black:#000000;
    --panel:#333333;
    --card:#262626;
    --blue:#2a7bbf;
    --blue-light:#3b8ed6;
    --hero-a:#2f4f72;
    --hero-b:#5f86b3;
    --white:#ffffff;
    --rule:#3a3a3a;
  }
  *{box-sizing:border-box;margin:0;padding:0}
  html,body{width:1200px;height:1200px;overflow:hidden;background:var(--white)}
  body{position:relative;font-family:'Lato',Arial,sans-serif;color:var(--white)}
  .page{position:absolute;left:220px;top:0;width:759px;height:1198px;background:var(--panel);overflow:hidden}
  .page > *{position:absolute}

  /* header */
  .site-header{left:0;top:0;width:759px;height:46px;background:var(--black)}
  .brand{position:absolute;left:71px;top:8px;font-family:'Oswald',Arial,sans-serif;line-height:1}
  .brand-name{display:block;font-size:21px;font-weight:600;color:var(--white);letter-spacing:.5px}
  .brand-tag{display:block;font-size:8px;font-weight:400;color:var(--blue-light);letter-spacing:2px;margin-top:1px}
  .main-nav{position:absolute;top:16px;left:0;width:759px;font-family:'Oswald',Arial,sans-serif;font-size:8px;font-weight:500}
  .main-nav a{position:absolute;color:var(--white);text-decoration:none;white-space:nowrap}
  .main-nav a.active{color:var(--blue-light)}

  /* hero */
  .hero{left:0;top:46px;width:759px;height:97px;background:linear-gradient(90deg,var(--hero-a),var(--hero-b) 45%,var(--hero-a) 60%,var(--hero-b))}
  .hero-title{left:0;top:52px;width:759px;text-align:center;font-family:'Oswald',Arial,sans-serif;font-weight:600;font-size:48px;line-height:1;letter-spacing:.5px}
  .hero-rule{left:358px;top:117px;width:44px;height:2px;background:var(--white)}

  /* portrait */
  .guard-photo{left:0;top:233px;width:260px;height:728px;background:linear-gradient(180deg,#3a3a3a 0%,#1b1b1b 20%,#0d0d0d 100%);border-radius:120px 120px 0 0}

  /* service cards */
  .service-card{width:196px;background:var(--card);border-radius:4px;text-align:center;padding:0 20px}
  .service-icon{position:absolute;left:75px;top:-21px;width:46px;height:46px;border-radius:50%;background:var(--blue);display:flex;align-items:center;justify-content:center}
  .service-title{font-family:'Oswald',Arial,sans-serif;font-weight:600;font-size:9px;margin-top:42px;letter-spacing:.2px}
  .service-text{font-size:7.6px;line-height:11px;margin-top:7px;color:var(--white)}
  .learn-more{position:absolute;left:0;width:196px;font-family:'Oswald',Arial,sans-serif;font-size:9.5px;font-weight:500;color:var(--blue-light);text-decoration:none}

  /* footer */
  .site-footer{left:0;top:961px;width:759px;height:237px;background:var(--black)}
  .site-footer > *{position:absolute}
  .footer-brand{left:71px;top:34px;font-family:'Oswald',Arial,sans-serif;line-height:1}
  .footer-brand .brand-name{font-size:34px;font-weight:600}
  .footer-brand .brand-tag{font-size:15px;letter-spacing:3px;margin-top:2px}
  .footer-about{left:71px;top:110px;width:190px;font-size:8.6px;line-height:12.5px;font-weight:700}
  .footer-links{left:367px;top:37px;list-style:none;font-size:8.6px;font-weight:700;line-height:14.2px}
  .footer-links li::before{content:"";display:inline-block;width:4px;height:4px;border-radius:50%;background:var(--blue-light);margin-right:5px;vertical-align:middle}
  .contact-item{left:587px;display:flex;gap:6px;font-size:8.6px;font-weight:700;line-height:12.5px}
  .contact-item svg{flex:none}
  .footer-rule{left:71px;top:200px;width:617px;height:1px;background:var(--rule)}
  .copyright{left:0;top:212px;width:759px;text-align:center;font-size:8.6px;font-weight:700}
  .copyright span{color:var(--blue-light)}
</style>
</head>
<body>
<div class="page">

  <header class="site-header">
    <div class="brand"><span class="brand-name">VEMRA</span><span class="brand-tag">SECURITY</span></div>
    <nav class="main-nav">
      <a href="#" style="left:333px">Home</a>
      <a href="#" style="left:376px">About Us</a>
      <a href="#" style="left:430px">Guyana Security Overview</a>
      <a href="#" class="active" style="left:539px">Services</a>
      <a href="#" style="left:588px">Contact Us</a>
    </nav>
  </header>

  <div class="hero" role="img" aria-label="Blue-toned photo of a bodyguard in a suit in front of a glass building"></div>
  <h1 class="hero-title">SERVICES</h1>
  <div class="hero-rule"></div>

  <div class="guard-photo" role="img" aria-label="Photo of a security guard in a black T-shirt and sunglasses with arms crossed"></div>

  <article class="service-card" style="left:281px;top:217px;height:177px">
    <div class="service-icon"><svg width="18" height="18" viewBox="0 0 18 18"><rect x="1" y="1" width="16" height="16" rx="2" fill="#fff"/><path d="M9 4v10M4 9h10" stroke="#2a7bbf" stroke-width="3"/></svg></div>
    <h2 class="service-title">Casualty Evacuation</h2>
    <p class="service-text">VEMRA is the only private organisation in Guyana with three fully equipped ambulances, stocked and manned and on standby for your personnel should you choose VEMRA to provide cover for you during your operations in Guyana.</p>
    <a class="learn-more" href="#" style="top:139px">LEARN MORE ➔</a>
  </article>

  <article class="service-card" style="left:493px;top:217px;height:177px">
    <div class="service-icon"><svg width="18" height="20" viewBox="0 0 18 20"><path d="M6 1h6l-2 4H8z" fill="#fff"/><ellipse cx="9" cy="13" rx="8" ry="6.5" fill="#fff"/><text x="9" y="16.5" text-anchor="middle" font-size="9" font-family="Arial,sans-serif" font-weight="700" fill="#2a7bbf">$</text></svg></div>
    <h2 class="service-title" style="margin-top:44px">Kidnap and Ransom Support</h2>
    <p class="service-text">VEMRA can work with your risk management teams, insurers and local security forces to advise on response strategies and if necessary provide specialist teams to support ground operations and recovery scenarios.</p>
    <a class="learn-more" href="#" style="top:139px">LEARN MORE ➔</a>
  </article>

  <article class="service-card" style="left:281px;top:450px;height:180px">
    <div class="service-icon"><svg width="14" height="20" viewBox="0 0 14 20"><rect x="9" y="0" width="2" height="5" fill="#fff"/><rect x="1" y="4" width="12" height="15" rx="2" fill="#fff"/><rect x="3.5" y="7" width="7" height="4" fill="#2a7bbf"/></svg></div>
    <h2 class="service-title">Static Security</h2>
    <p class="service-text">Whether it is ports, installations or work sites, a credible security force with integrated technology systems is vital to protecting your assets and personnel in their place of work</p>
    <a class="learn-more" href="#" style="top:137px">LEARN MORE ➔</a>
  </article>

  <article class="service-card" style="left:493px;top:452px;height:180px">
    <div class="service-icon"><svg width="22" height="16" viewBox="0 0 22 16"><path d="M1 2h20v6H11l-1 2H8l-2 5H2l2-7H1z" fill="#fff"/></svg></div>
    <h2 class="service-title" style="margin-top:50px">Armed Close Protection</h2>
    <p class="service-text">High crime rates during politically charged times poses a very real threat to foreign workers</p>
    <a class="learn-more" href="#" style="top:139px">LEARN MORE ➔</a>
  </article>

  <article class="service-card" style="left:282px;top:691px;height:179px">
    <div class="service-icon"><svg width="20" height="18" viewBox="0 0 20 18"><path d="M1 2h6M13 2h6M4 2v3M16 2v3" stroke="#fff" stroke-width="2"/><rect x="6" y="5" width="8" height="6" rx="1.5" fill="#fff"/><path d="M3 7h3M14 7h3M6 11l-3 5M14 11l3 5" stroke="#fff" stroke-width="2"/></svg></div>
    <h2 class="service-title" style="font-size:10.5px;margin-top:48px">Asset Protection</h2>
    <p class="service-text" style="font-size:8.6px;line-height:13px;margin-top:8px">Well trained security drivers supplemented with fixed wing drones can clear and secure routes providing safe passage anywhere in the region.</p>
    <a class="learn-more" href="#" style="top:137px">LEARN MORE ➔</a>
  </article>

  <article class="service-card" style="left:497px;top:690px;height:179px">
    <div class="service-icon"><svg width="20" height="16" viewBox="0 0 20 16"><path d="M4 2h12l2 6H2z" fill="#fff"/><rect x="1" y="7" width="18" height="6" rx="1.5" fill="#fff"/><rect x="2" y="13" width="3" height="3" fill="#fff"/><rect x="15" y="13" width="3" height="3" fill="#fff"/><circle cx="5" cy="10" r="1.3" fill="#2a7bbf"/><circle cx="15" cy="10" r="1.3" fill="#2a7bbf"/></svg></div>
    <h2 class="service-title" style="margin-top:53px">Mobile Security</h2>
    <p class="service-text">VEMRA can move your personnel to and from their work locations securely or to and from airports and heliports</p>
    <a class="learn-more" href="#" style="top:134px">LEARN MORE ➔</a>
  </article>

  <footer class="site-footer">
    <div class="footer-brand brand" style="position:absolute"><span class="brand-name">VEMRA</span><span class="brand-tag">SECURITY</span></div>
    <p class="footer-about">VEMRA is a Trading Division of Marovell Developments Inc, a duly incorporated and registered Guyanese corporation with Company Registration Number XXXXX and located at XXXXXXXXX.</p>
    <ul class="footer-links">
      <li>Home</li>
      <li>About Us</li>
      <li>Guyana Security Overview</li>
      <li>Services</li>
      <li>Contact Us</li>
      <li>Useful Links</li>
    </ul>
    <div class="contact-item" style="top:38px">
      <svg width="14" height="18" viewBox="0 0 14 18"><path d="M7 0C3 0 0 3 0 7c0 5 7 11 7 11s7-6 7-11C14 3 11 0 7 0z" fill="#2a7bbf"/><circle cx="7" cy="7" r="2.5" fill="#000"/></svg>
      <span>120 Front Street<br>Riverton, OR 97301</span>
    </div>
    <div class="contact-item" style="top:86px">
      <svg width="17" height="15" viewBox="0 0 17 15"><path d="M0 6L17 0 12 15 8 9z" fill="#2a7bbf"/></svg>
      <span>desk@vemralink.net</span>
    </div>
    <div class="contact-item" style="top:124px">
      <svg width="15" height="15" viewBox="0 0 15 15"><path d="M2 0l3 0 1.5 4-2 1.5c1 2 2.5 3.5 4.5 4.5L10.5 8l4 1.5v3c0 1.5-1 2.5-2.5 2.5C5.5 14.5.5 9.5 0 3 0 1.5.8 0 2 0z" fill="#2a7bbf"/></svg>
      <span>+1 (555) 014-7890</span>
    </div>
    <div class="footer-rule"></div>
    <p class="copyright">© 2020 VEMRA. All Rights Reserved. <span>Terms. Privacy Policy.</span></p>
  </footer>

</div>
</body>
</html>
```